Flyer Design Print Ad for Clothing Store

We are a modest women's clothing store. We are looking for a print ad 90*134 mm that is attention grabbing and can serve as a template for us going forward. We cannot use pictures of actual women. We need it to include our logo, store hours, physical address, website, phone number. We would use this template and change the call to action as necessary e. g. BOGO Sale, 30% off, flash sale, summer sale etc. Our colors are black and white and our fonts are Bodoni sans and Athens.

Target Market(s)

Women from teen to age 70

Industry/Entity Type

Women's clothing

Font styles to use
Other font styles liked:
• Athens, Bodoni Sans

Requirements
Must have
• Our, logo, phone number, website, address and store hours
Nice to have
• I'd like something that's not just our flat logo but something that will make someone pause to look
Should not have
• Pictures of women

```html
<!DOCTYPE html>
<html lang="en">
<head>
<meta charset="utf-8">
<title>Women's Clothing Store Flyer</title>
<link href="https://fonts.googleapis.com/css2?family=Italiana&family=Cormorant+Garamond:wght@600&family=Open+Sans:wght@400;700&display=swap" rel="stylesheet">
<style>
  :root {
    --backdrop: #c2c2c2;
    --cream: #f1e9d8;
    --cream-light: #f5efe2;
    --sand: #e6d6b8;
    --camel: #d2b48a;
    --mustard: #b98a34;
    --mauve: #bba79e;
    --ink: #111111;
    --paper-white: #ffffff;
  }
  * { margin: 0; padding: 0; box-sizing: border-box; }
  html, body { width: 1200px; height: 900px; overflow: hidden; }
  body { background: var(--backdrop); position: relative; font-family: "Italiana", serif; color: var(--ink); }

  .flyer { position: absolute; top: 133px; width: 425px; height: 634px; overflow: hidden; background: var(--cream); }
  .flyer--front { left: 187px; }
  .flyer--back { left: 653px; }

  .photo { position: absolute; }
  .flyer--front .photo {
    inset: 0;
    background:
      radial-gradient(ellipse 55% 45% at 80% 78%, var(--mustard) 0%, rgba(185,138,52,0) 70%),
      radial-gradient(ellipse 35% 40% at 95% 88%, var(--mauve) 0%, rgba(187,167,158,0) 75%),
      radial-gradient(ellipse 60% 40% at 65% 45%, var(--camel) 0%, rgba(210,180,138,0) 70%),
      linear-gradient(180deg, var(--cream-light) 0%, var(--cream) 40%, var(--sand) 100%);
  }
  .flyer--back .photo {
    left: 0; top: 0; width: 425px; height: 538px;
    background:
      radial-gradient(ellipse 70% 30% at 55% 90%, var(--camel) 0%, rgba(210,180,138,0) 70%),
      linear-gradient(180deg, var(--sand) 0%, var(--cream) 45%, var(--sand) 100%);
  }
  .band { position: absolute; left: 0; top: 538px; width: 425px; height: 96px; background: var(--cream); }

  .frame { position: absolute; left: 0; top: 0; width: 425px; height: 634px; }

  .center { position: absolute; left: 0; right: 0; text-align: center; }
  .front-column { left: 0; right: 130px; }

  .brand-mark { position: absolute; left: 113px; top: 49px; width: 67px; height: 67px; border-radius: 50%; background: var(--ink); }
  .brand-name { top: 124px; font-family: "Cormorant Garamond", serif; font-weight: 600; font-size: 19px; letter-spacing: 6px; padding-left: 6px; }

  .headline { top: 186px; font-weight: 400; font-size: 42px; line-height: 48px; }
  .offers { top: 344px; font-size: 19px; line-height: 20px; }
  .offers .tilde { display: block; font-size: 16px; height: 20px; line-height: 20px; }

  .url-pill {
    position: absolute; left: 115px; width: 200px; background: var(--ink); color: var(--paper-white);
    text-align: center;
    font-family: "Cormorant Garamond", serif; font-weight: 600; font-size: 14px; letter-spacing: 0.5px;
  }
  .flyer--front .url-pill { top: 590px; height: 27px; line-height: 27px; border-radius: 14px 14px 0 0; }
  .flyer--back .url-pill { top: 586px; height: 48px; line-height: 30px; left: 116px; border-radius: 16px 16px 0 0; }

  .back-title { top: 64px; font-weight: 400; font-size: 31px; line-height: 36px; }
  .hanger { position: absolute; left: 180px; top: 128px; width: 74px; height: 50px; }
  .back-offers { top: 199px; font-size: 22px; line-height: 29px; }

  .info-card { position: absolute; left: 78px; top: 400px; width: 275px; height: 160px; background: var(--cream); border-radius: 24px 24px 0 0; }
  .contact { top: 420px; font-family: "Open Sans", sans-serif; font-size: 14px; line-height: 19.5px; }
  .contact .phone { font-weight: 700; font-size: 20px; line-height: 26px; }
  .contact .bold { font-weight: 700; }
  .contact .rtl { direction: rtl; unicode-bidi: plaintext; }
  .contact .buses { font-size: 10px; line-height: 18px; }
</style>
</head>
<body>

  <section class="flyer flyer--front" aria-label="Flyer front">
    <div class="photo" role="img" aria-label="Photo of knitwear sweaters in cream, mustard and mauve hanging on wooden hangers from a white clothes rail"></div>
    <svg class="frame" viewBox="0 0 425 634" aria-hidden="true">
      <defs>
        <linearGradient id="frontFade" x1="0" y1="0" x2="0" y2="1">
          <stop offset="0.25" stop-color="#fff" stop-opacity="0"/>
          <stop offset="0.5" stop-color="#fff" stop-opacity="0.9"/>
        </linearGradient>
      </defs>
      <path d="M27 160 V585 Q27 625 67 625 H375 Q415 625 415 585 V155" fill="none" stroke="url(#frontFade)" stroke-width="1.5"/>
      <path d="M40 160 V580 Q40 618 78 618 H368 Q406 618 406 580 V155" fill="none" stroke="url(#frontFade)" stroke-width="2.5"/>
    </svg>

    <div class="brand-mark"></div>
    <div class="center front-column brand-name">LUMELLE</div>

    <h1 class="center front-column headline">WOMEN'S<br>CLOTHING<br>STORE</h1>

    <div class="center front-column offers">
      <span class="tilde">~</span>BOGO SALE
      <span class="tilde">~</span>30% OFF
      <span class="tilde">~</span>FLASH SALE
      <span class="tilde">~</span>SUMMER SALE
      <span class="tilde">~</span>
    </div>

    <div class="url-pill">www.lumelle-style.com</div>
  </section>

  <section class="flyer flyer--back" aria-label="Flyer back">
    <div class="photo" role="img" aria-label="Photo of light sweaters on wooden hangers along a white clothes rail against a warm beige wall"></div>
    <div class="band"></div>
    <svg class="frame" viewBox="0 0 425 634" aria-hidden="true">
      <defs>
        <linearGradient id="backFade" x1="0" y1="0" x2="0" y2="1">
          <stop offset="0.6" stop-color="#fff" stop-opacity="0.9"/>
          <stop offset="0.85" stop-color="#fff" stop-opacity="0"/>
        </linearGradient>
      </defs>
      <path d="M16 540 V60 Q16 15 60 15 H365 Q410 15 410 60 V540" fill="none" stroke="url(#backFade)" stroke-width="1.5"/>
      <path d="M23 540 V66 Q23 22 66 22 H360 Q403 22 403 66 V540" fill="none" stroke="url(#backFade)" stroke-width="2.5"/>
    </svg>

    <h2 class="center back-title">WOMEN'S CLOTHING<br>STORE</h2>
    <svg class="hanger" viewBox="0 0 74 50" aria-hidden="true">
      <path d="M33 8 Q33 2 38 2 Q43 2 43 7 Q43 11 37 13 V17 L1 48 H73 L37 17" fill="none" stroke="#111" stroke-width="1.2" stroke-linejoin="round"/>
    </svg>
    <div class="center back-offers">~ BOGO Sale ~ 30% off ~<br>~ Flash sale ~ Summer sale ~</div>

    <div class="info-card"></div>
    <div class="center contact">
      <div class="phone">tel. 000 000 00 00</div>
      <div class="bold rtl">מרכז מסחרי גבעת הארז</div>
      <div class="bold">Cedar Hill Shopping Center</div>
      <div class="rtl">(מעל קפה לימון)</div>
      <div class="rtl">ניתן להגיע גם משדרות הארז 16</div>
      <div>S-Th: 10.00-19.00 :<span class="rtl">א-ה</span></div>
      <div class="buses">Buses 3, 8, 14, 17, 26, 31, 44, 50, 63, 72, 80</div>
    </div>

    <div class="url-pill">www.lumelle-style.com</div>
  </section>

</body>
</html>
```